Selka Marven Photography Business Card

I need a new business card/ possibly design to use for other marking materials ... I have included my logo below in a few different colors, but can also provide the logo in additional colors and sizes. I would love a card the expresses clean, simple and classy.

Target Market(s)

Portrait photography clients, child photography clients

Industry/Entity Type

Photographer

Contact Information for Business Card

Selka Marven Photography, Larkmoor MA, www.selkamarvenphotography-demo.com
T. 555-203-1946 E. selkamarvenphoto@mailbox-demo.com

Colors
33b8a4
eea4c8
5c5c5c

Requirements
Must have
• I would like to include my logo on card.
Nice to have
• I also like the color brown as well as the choices below. I would like a simple, elegant card, something classy.

```html
<!DOCTYPE html>
<html lang="en">
<head>
<meta charset="utf-8">
<title>Selka Marven Photography – Business Card</title>
<link href="https://fonts.googleapis.com/css2?family=Bebas+Neue&family=Open+Sans:wght@400;600&display=swap" rel="stylesheet">
<style>
  :root {
    --backdrop: #e4e4e4;
    --card-dark: #58585a;
    --card-light: #fbfbfb;
    --ink: #3d3d3d;
    --ink-soft: #555555;
    --accent: #d9a0dc;
    --divider: #4a4a4a;
  }
  * { margin: 0; padding: 0; box-sizing: border-box; }
  html, body { width: 1200px; height: 904px; overflow: hidden; }
  body {
    background: var(--backdrop);
    position: relative;
    font-family: "Open Sans", sans-serif;
  }
  .card {
    position: absolute;
    width: 560px;
    height: 320px;
    border-radius: 3px;
    box-shadow: 0 6px 18px rgba(0,0,0,0.18);
    overflow: hidden;
  }
  .card-front {
    left: 150px; top: 110px;
    background: var(--card-dark);
    display: flex; flex-direction: column;
    align-items: center; justify-content: center;
  }
  .brand-name {
    font-family: "Open Sans", sans-serif;
    font-weight: 600;
    color: var(--accent);
    text-align: center;
    line-height: 1.25;
  }
  .brand-name .primary { display: block; font-size: 40px; letter-spacing: 2px; }
  .brand-name .secondary { display: block; font-size: 20px; letter-spacing: 6px; text-transform: uppercase; }
  .card-back {
    left: 490px; top: 470px;
    background: var(--card-light);
  }
  .accent-band {
    position: absolute; left: 0; right: 0; bottom: 0;
    height: 12px; background: var(--accent);
  }
  .back-content {
    position: absolute; left: 18px; right: 18px; top: 112px;
    display: flex; align-items: stretch; justify-content: center;
    gap: 12px;
  }
  .identity {
    text-align: right;
    display: flex; flex-direction: column; justify-content: flex-end;
    padding-bottom: 2px;
  }
  .identity-name {
    font-family: "Bebas Neue", sans-serif;
    font-size: 27px; color: var(--ink); letter-spacing: 0.3px; line-height: 1;
    white-space: nowrap;
  }
  .identity-place { font-size: 12px; color: var(--ink-soft); margin-top: 2px; white-space: nowrap; }
  .divider {
    width: 2px; background: var(--divider); flex: none;
  }
  .contact-list {
    list-style: none;
  }
  .contact-list li {
    display: flex; align-items: center; gap: 7px;
    font-size: 11.5px; color: var(--ink-soft);
    height: 21px; white-space: nowrap;
  }
  .contact-icon { width: 13px; height: 13px; flex: none; }
</style>
</head>
<body>
  <section class="card card-front" aria-label="Card front">
    <div class="brand-name">
      <span class="primary">Selka Marven</span>
      <span class="secondary">Photography</span>
    </div>
  </section>

  <section class="card card-back" aria-label="Card back">
    <div class="back-content">
      <div class="identity">
        <div class="identity-name">Selka Marven Photography</div>
        <div class="identity-place">Larkmoor MA</div>
      </div>
      <div class="divider"></div>
      <ul class="contact-list">
        <li>
          <svg class="contact-icon" viewBox="0 0 16 16" aria-hidden="true">
            <circle cx="8" cy="8" r="8" fill="var(--accent)"/>
            <path d="M5 4.5c.5-.5 1-.4 1.3.1l.7 1.2c.2.4.1.8-.2 1l-.4.3c.4.9 1.1 1.6 2 2l.3-.4c.3-.3.7-.4 1-.2l1.2.7c.5.3.6.8.1 1.3-.8.8-2 .9-3.2.2C6.4 9.8 5.2 8.6 4.6 7.3 4 6.2 4.2 5.3 5 4.5z" fill="#fff"/>
          </svg>
          555-203-1946
        </li>
        <li>
          <svg class="contact-icon" viewBox="0 0 16 16" aria-hidden="true">
            <circle cx="8" cy="8" r="8" fill="var(--accent)"/>
            <rect x="3.8" y="5" width="8.4" height="6" rx="0.8" fill="#fff"/>
            <path d="M4 5.4 8 8.4l4-3" fill="none" stroke="var(--accent)" stroke-width="1"/>
          </svg>
          selkamarvenphoto@mailbox-demo.com
        </li>
        <li>
          <svg class="contact-icon" viewBox="0 0 16 16" aria-hidden="true">
            <circle cx="8" cy="8" r="8" fill="var(--accent)"/>
            <g fill="none" stroke="#fff" stroke-width="1">
              <circle cx="8" cy="8" r="4"/>
              <ellipse cx="8" cy="8" rx="1.8" ry="4"/>
              <path d="M4 8h8"/>
            </g>
          </svg>
          www.selkamarvenphotography-demo.com
        </li>
      </ul>
    </div>
    <div class="accent-band"></div>
  </section>
</body>
</html>
```